Brochure for Specialist Divorce Support

1. I want an A4 three fold brochure or DL to promote my business and services.
My market are people going through divorce and are usually feeling very overwhelmed and therefore not functioning very well - both men and women, age early forties,
2. Colours – variety of blues and lime greens but you choose if you need a contrast e.g. orange
3. Images – happy single families
4. Theme - could you make it around water please - soothing
5. Logos – MJT &; MJR (I will attach)
6. I have a lot of content so maybe not too busy but still professional feel +
warm and reassuring
7. I'm attaching -

- a draft brochure I put together using a Microsoft template
- a word document with extra details
- plus two logos to do with my qualifications
- and some images for you to choose from

7. I want to use this as a template for some other brochures -> more work for
the winner.

Target Market(s)

Men and women usually in their early forties with primary school aged children i.e 5 to 12 years old.
They are going through a divorce and very upset, Maybe losing contact with their children and their way of life as they know it is disappearing. They are in turmoil and not functioning as well as they usually do.

Industry/Entity Type

Business

Font styles to use
Sans Serif

Colors
34a7d7
abd037
3277b5

Requirements
Must have
• I want the brochure to be three folds with the center the full A4
• Could you make the theme around water please.
• I will upload some photos for you to use if you want,

```html
<!DOCTYPE html>
<html lang="en">
<head>
<meta charset="utf-8">
<title>MJR Tailored Divorce Coaching Brochure</title>
<link href="https://fonts.googleapis.com/css2?family=Cinzel:wght@600&family=Lato:ital,wght@0,400;0,700;1,400&family=Montserrat:wght@600;700&family=Oswald:wght@500&display=swap" rel="stylesheet">
<style>
  :root{
    --sky:#34a7d7;
    --lime:#abd037;
    --ocean:#3277b5;
    --navy:#2c3470;
    --ink:#3a3a3a;
    --paper:#ffffff;
    --stage:#eef1f4;
  }
  *{box-sizing:border-box;margin:0;padding:0}
  html,body{width:1200px;height:1200px;overflow:hidden;background:var(--stage)}
  .brochure{position:absolute;left:0;top:176px;width:1200px;height:848px;display:flex;box-shadow:0 10px 30px rgba(0,0,0,.15)}
  .panel{position:relative;width:400px;height:848px;overflow:hidden}
  .panel--services{background:var(--paper)}
  .panel--quotes{background:linear-gradient(180deg,#3aaede 0%,var(--sky) 60%,#2f9bcc 100%)}
  .panel--cover{background:linear-gradient(90deg,#f2f2f2 0%,var(--paper) 30%)}

  .pill{position:absolute;left:36px;background:var(--sky);color:#fff;font:600 16px/1 "Cinzel",serif;
        padding:9px 28px;border-radius:18px;letter-spacing:.5px}
  .pill--services{top:40px}
  .pill--testimonial{top:258px;left:60px}
  .body-copy{position:absolute;left:44px;right:36px;font:400 12.5px/1.28 "Lato",sans-serif;color:var(--ink);text-align:justify}
  .body-copy--services{top:92px}
  .body-copy--testimonial{top:310px;left:64px}
  .signature{display:block;text-align:right;margin-top:6px}

  .photo-band{position:absolute;left:0;bottom:0;width:400px;height:300px}

  .brand{position:absolute;font:700 44px/1 "Montserrat",sans-serif;color:var(--navy);letter-spacing:1px}
  .brand-dot{display:inline-block;width:10px;height:10px;border-radius:50%;background:var(--navy);margin-left:6px;vertical-align:middle}
  .panel--quotes .brand{left:0;right:0;top:56px;text-align:center}
  .partner-tag{position:absolute;left:100px;top:140px;width:200px;height:70px;background:#fff;display:flex;align-items:center;justify-content:center;
               font:700 30px/1 "Montserrat",sans-serif;color:#c8242b}
  .quotes{position:absolute;left:36px;right:36px;top:268px;list-style:none}
  .quotes li{font:italic 400 12.5px/1.35 "Lato",sans-serif;color:#e9f6fb;text-align:center;margin-bottom:18px;position:relative;padding-left:18px}
  .quotes li::before{content:"";position:absolute;left:0;top:3px;width:10px;height:8px;border-radius:3px;background:var(--lime)}
  .contact-card{position:absolute;left:28px;right:28px;top:600px;height:210px;background:#fff;border-radius:18px;
                padding:24px 26px;font:400 13px/1.5 "Lato",sans-serif;color:var(--ink)}

  .panel--cover .brand{left:0;right:0;top:60px;text-align:center;font-size:52px}
  .cover-photo{position:absolute;left:0;top:0;width:400px;height:848px}
  .cover-title{position:absolute;left:40px;right:30px;top:650px}
  .cover-kicker{font:700 26px/1 "Montserrat",sans-serif;color:#222;letter-spacing:2px}
  .cover-headline{font:500 50px/1.05 "Oswald",sans-serif;color:var(--sky);margin-top:8px}
  .cover-web{font:400 19px/1 "Montserrat",sans-serif;color:#444;letter-spacing:2px;margin-top:28px;padding-left:40px}
</style>
</head>
<body>
<main class="brochure">

  <section class="panel panel--services">
    <h2 class="pill pill--services">My services</h2>
    <p class="body-copy body-copy--services">Specialist divorce support to suit your needs Pre-mediation coaching helping you prepare and achieve more positive outcomes to avoid going to court Collaborative law coaching to increase crucial skills so you can participate more constructively in negotiations Delivery of MJT Conflict Insight Profile giving you real feedback on the constructive and destructive behaviours you choose during conflict situations to facilitate more productive discussions Corporate Conflict Management Training</p>
    <h2 class="pill pill--testimonial">Testimonial</h2>
    <p class="body-copy body-copy--testimonial">"After many cups of coffee and long hours of listening to me, my very good friend suggested I speak to Helena, a divorce coach. I was a bit skeptical, especially when a phone session was suggested. From my first phone session I felt empowered. It gave me a sense of direction, assisted me to set realistic goals and action plans. Most importantly it aided my self esteem.<br>Divorce is overwhelming. Talking to a caring professional like Helena helped me acknowledge my priorities and a way to achieve them. Thank you Helena."<span class="signature">Marisa - Cccccc, Smmmmm. AAA</span></p>
    <svg class="photo-band" viewBox="0 0 400 300">
      <defs>
        <linearGradient id="giftPhoto" x1="0" y1="0" x2="1" y2="1">
          <stop offset="0" stop-color="#e8d2b8"/><stop offset=".5" stop-color="#d9b39a"/><stop offset="1" stop-color="#3aa9a0"/>
        </linearGradient>
      </defs>
      <path d="M0 300 L0 150 Q180 20 400 40 L400 300 Z" fill="url(#giftPhoto)" role="img" aria-label="Photo of a smiling mother and daughter opening a gift"/>
      <path d="M0 120 Q180 -5 400 14" fill="none" stroke="var(--lime)" stroke-width="7"/>
      <path d="M0 140 Q180 12 400 30" fill="none" stroke="var(--sky)" stroke-width="9"/>
    </svg>
  </section>

  <section class="panel panel--quotes">
    <div class="brand">MJR<span class="brand-dot"></span></div>
    <div class="partner-tag">MJT</div>
    <ul class="quotes">
      <li>Even the most together person can be totally unprepared for the emotional overwhelm that divorce can bring, regardless if they are the one who made the decision to leave</li>
      <li>Every divorce is different and families going forward will be different. I try to get my client to see or find ways they can co-parent as opposed to being one of two single parents</li>
      <li>Often family and friends can try to influence decisions based on what they see as best, so you can feel under an enormous pressure to keep them happy. Coaching offers an objective and neutral sounding board there just for you</li>
      <li>Everyone is different and move through these stages at their own pace</li>
    </ul>
    <div class="contact-card">
      Full details on my website<br>
      or email: Helena@<br>
      Helena ..........<br>
      MJR Certified Divorce Coach<br>
      Harmonia Trained Conflict Coach<br>
      Cert IV in Training &amp; Assessment<br>
      Accredited in MJT Conflict Insight Profile<br>
      BA (Ind. Relations) (UVVV)
    </div>
  </section>

  <section class="panel panel--cover">
    <svg class="cover-photo" viewBox="0 0 400 848">
      <defs>
        <linearGradient id="familyPhoto" x1="0" y1="0" x2="1" y2="1">
          <stop offset="0" stop-color="#b9c98a"/><stop offset=".45" stop-color="#c9a78a"/><stop offset="1" stop-color="#8f9a6a"/>
        </linearGradient>
      </defs>
      <path d="M400 150 Q200 160 110 330 Q60 460 120 620 Q280 600 400 500 Z" fill="url(#familyPhoto)" role="img" aria-label="Photo of a smiling father carrying his daughter on his back outdoors"/>
      <path d="M400 122 Q190 130 92 320 Q40 460 100 630" fill="none" stroke="var(--lime)" stroke-width="7"/>
      <path d="M400 138 Q200 145 102 325 Q50 460 112 625" fill="none" stroke="var(--sky)" stroke-width="8"/>
      <path d="M90 640 Q260 620 400 500" fill="none" stroke="var(--lime)" stroke-width="6"/>
      <path d="M112 628 Q275 606 400 510" fill="none" stroke="var(--sky)" stroke-width="7"/>
    </svg>
    <div class="brand">MJR<span class="brand-dot"></span></div>
    <div class="cover-title">
      <h1 class="cover-kicker">TAILORED DIVORCE</h1>
      <p class="cover-headline">COACHING / SUPPORT</p>
      <p class="cover-web">mjrcoaching.example</p>
    </div>
  </section>

</main>
</body>
</html>
```